Skincare Line needs a label design

I need a label design for a new company based on Vancouver Island, Canada called 'Velvet Orlish" We have formulated a skincare line for those with hyperpigmentation (sunspots, age spots, freckles etc) and also for those wanting to reduce redness caused from acne, rosacea, eczema, psoriasis and other skin conditions. We would like to see designs that use earth based colors as we have used microgreens as our inspiration and they come in all sorts of colors from deep greens to fuscia pink and bright yet deep yellows, Maroons, and purples are also quite common in these tiny plants. The final design should communicate high-end, classy yet effective ingredients.

Target Market(s)

Those with skin conditions such as eczema, acne rosacea and hyperpigmentation (sun spots, age spots, discoloration)

Industry/Entity Type

skincare line such as Cleanser, Toner, Serum, eye cream, facial cream

Logo Text

Velvet Orlish

Requirements
Must have
• Size of label is 1.914inches x 5.3835 inches
Nice to have
• nice to see color. I also like the microgreen I uploaded but it's not necessary.

```html
<!DOCTYPE html>
<html lang="en">
<head>
<meta charset="UTF-8">
<title>Velvet Orlish — Skincare Label</title>
<link rel="stylesheet" href="https://fonts.googleapis.com/css2?family=Cormorant+Garamond:wght@400&display=swap">
<style>
  :root {
    --page-bg: #ffffff;
    --label-magenta: #c8006f;
    --petal-bright: #e2008a;
    --petal-deep: #b8006a;
    --ink-white: #ffffff;
  }
  html, body {
    margin: 0;
    padding: 0;
    width: 775px;
    height: 1200px;
    overflow: hidden;
    background: var(--page-bg);
  }
  .canvas {
    position: relative;
    width: 775px;
    height: 1200px;
  }
  .label {
    position: absolute;
    left: 202px;
    top: 80px;
    width: 370px;
    height: 1040px;
    background: var(--label-magenta);
    overflow: hidden;
  }
  .label__botanical {
    position: absolute;
    left: 0;
    top: 0;
    width: 370px;
    height: 560px;
    background:
      radial-gradient(ellipse 110px 150px at 150px 150px, rgba(226,0,138,0.55), transparent 70%),
      radial-gradient(ellipse 80px 100px at 300px 440px, rgba(226,0,138,0.5), transparent 70%),
      radial-gradient(ellipse 90px 120px at 60px 120px, rgba(184,0,106,0.4), transparent 70%);
  }
  .label__guides {
    position: absolute;
    left: 0;
    top: 0;
  }
  .label__name {
    position: absolute;
    left: 0;
    top: 740px;
    width: 370px;
    margin: 0;
    text-align: center;
    font-family: "Cormorant Garamond", serif;
    font-weight: 400;
    font-size: 42px;
    line-height: 1.15;
    letter-spacing: 0.22em;
    text-transform: uppercase;
    color: var(--ink-white);
  }
  .label__name span {
    display: block;
    padding-left: 0.22em;
  }
</style>
</head>
<body>
  <main class="canvas">
    <section class="label">
      <div class="label__botanical" role="img" aria-label="Soft tonal illustration of magenta microgreen leaves"></div>

      <svg class="label__guides" width="370" height="1040" viewBox="0 0 370 1040" aria-hidden="true">
        <line x1="185" y1="335" x2="185" y2="504" stroke="#ffffff" stroke-width="1.5"/>
        <circle cx="185" cy="576" r="40" fill="#ffffff"/>
        <line x1="185" y1="648" x2="185" y2="716" stroke="#ffffff" stroke-width="1.5"/>
        <line x1="185" y1="897" x2="185" y2="990" stroke="#ffffff" stroke-width="1.5"/>
      </svg>

      <h1 class="label__name"><span>Velvet</span><span>Orlish</span></h1>
    </section>
  </main>
</body>
</html>
```